Simple web design project

We need a four page web design for a premier domestic cleaning company. We would like to see designs which use white and blue (the blue in the logo - which is attatched). Please could the tab for the pages be horizontal and at the top of the page. Our company logo is attached and should be included on each page. Ideally, we would like the foundations of each page to be the same, with the word content differing as required (word content attatched). Additionally we have attached a flyer which has been distributed to advertise our company. Please could all web designs illustrate the same professional message this flyer does.

Target Market(s)

females with higher than average income, aged 30-50. Have families and work 9-5.

Industry/Entity Type

It Company

Requirements
Must have
• logo on each page. Foundations of each page the same. phone number and email on the bottom of each page.
Should not have
• please no pictures of females cleaning.

```html
<!DOCTYPE html>
<html lang="en">
<head>
<meta charset="utf-8">
<title>Brookfield Cleaners – Premier Domestic Cleaners</title>
<link rel="stylesheet" href="https://fonts.googleapis.com/css2?family=PT+Sans:wght@400;700&family=PT+Sans+Narrow:wght@400;700&display=swap">
<style>
:root{
  --brand-blue:#2461ad;
  --panel-top:#3179cf;
  --panel-bottom:#2257a6;
  --text-dark:#24456f;
  --accent-orange:#f08a1c;
  --field-text:#3a6fb5;
  --search-grey:#e2e2e2;
  --white:#ffffff;
}
*{box-sizing:border-box;margin:0;padding:0}
html,body{width:1200px;height:1080px;overflow:hidden;background:var(--white)}
body{position:relative;font-family:"PT Sans",sans-serif;color:var(--text-dark)}
.edge-bar{position:absolute;left:0;width:1200px;height:6px;background:var(--brand-blue)}
.edge-bar--top{top:0}
.edge-bar--bottom{top:1074px}

.brand{position:absolute;left:182px;top:30px;width:260px;text-align:center}
.brand__row{display:flex;align-items:center;justify-content:center;gap:10px}
.brand__mark{width:26px;height:26px;border-radius:50%;background:var(--brand-blue)}
.brand__name{font-size:31px;font-weight:700;color:var(--brand-blue);line-height:1.2}
.brand__tagline{margin-top:12px;font-family:"PT Sans Narrow",sans-serif;font-size:17px;color:#1b2d4a;padding-left:18px}

.search{position:absolute;left:787px;top:36px;width:230px;height:29px;background:var(--search-grey);display:flex;align-items:center;justify-content:space-between;padding:0 8px 0 14px;font-size:12px;color:#444}
.main-nav{position:absolute;left:479px;top:89px;width:539px;height:27px;background:var(--brand-blue);display:flex}
.main-nav a{color:var(--white);text-decoration:none;font-size:12px;display:flex;align-items:center;justify-content:center;border-right:1px solid #1a4a8a}
.main-nav a:last-child{border-right:none}

.hero{position:absolute;left:167px;top:136px;width:863px;height:389px;border:1px solid #c9c9c9;background:linear-gradient(180deg,#eef1f3 0%,#dfe5ea 50%,#c4cad0 100%)}
.hero__dots{position:absolute;left:38px;bottom:14px;display:flex;gap:5px}
.hero__dots span{width:13px;height:13px;border-radius:50%;background:radial-gradient(circle at 40% 35%,#fff,#d8d8d8)}
.hero__dots span.is-active{background:var(--brand-blue)}

.info-panel{position:absolute;left:167px;top:536px;width:862px;height:271px;background:linear-gradient(180deg,var(--panel-top),var(--panel-bottom))}
.section-title{font-family:"PT Sans Narrow",sans-serif;font-size:22px;font-weight:400;color:var(--white);position:absolute}
.quote-title{left:28px;top:18px}
.field{position:absolute;left:29px;width:261px;background:var(--white);color:var(--field-text);font-size:12px;padding:6px 10px}
.field--name{top:63px;height:28px}
.field--email{top:98px;height:28px}
.field--message{top:134px;height:80px;padding-top:10px}
.submit-button{position:absolute;left:223px;top:227px;width:69px;height:24px;background:linear-gradient(180deg,#f9a233,#ee8012);color:#222;font-size:12px;display:flex;align-items:center;justify-content:center}
.services-title{left:346px;top:18px}
.services-rule{position:absolute;left:346px;top:54px;width:495px;height:1px;background:#163e78}
.services-photo{position:absolute;left:350px;top:87px;width:142px;height:131px;background:linear-gradient(160deg,#8e9a6a 0%,#b8a888 45%,#c79a62 100%)}
.services-copy{position:absolute;left:512px;top:84px;width:345px;color:var(--white);font-size:12px;line-height:22px}
.services-copy .types span{margin-right:12px}
.services-copy p.desc{margin-top:6px;line-height:18px}
.read-more{display:inline-block;margin-top:10px;font-size:14px;color:var(--white);text-decoration:none}

.welcome{position:absolute;left:168px;top:824px;width:860px}
.welcome__title{font-family:"PT Sans Narrow",sans-serif;font-size:22px;font-weight:400;color:var(--brand-blue)}
.welcome__text{margin-top:12px;font-size:12px;line-height:22px;color:var(--text-dark)}
.welcome__perks{margin-top:14px;font-size:12px;color:var(--accent-orange)}
.welcome__perks span.sep{margin:0 7px}

.site-footer{position:absolute;left:167px;top:966px;width:862px;height:105px;background:linear-gradient(180deg,var(--panel-top),var(--panel-bottom));color:var(--white);font-size:12px}
.footer-links{position:absolute;left:23px;top:22px;line-height:22px}
.footer-links .sep{margin:0 6px}
.footer-contact{position:absolute;right:28px;top:32px;text-align:right;line-height:22px}
</style>
</head>
<body>
<div class="edge-bar edge-bar--top"></div>

<header>
  <div class="brand">
    <div class="brand__row"><span class="brand__mark"></span><span class="brand__name">Brookfield Cleaners</span></div>
    <div class="brand__tagline">Premier Domestic Cleaners</div>
  </div>
  <div class="search">
    <span>Search</span>
    <svg width="18" height="18" viewBox="0 0 18 18" aria-hidden="true"><circle cx="7" cy="7" r="5" fill="none" stroke="#666" stroke-width="1.6"/><line x1="10.5" y1="10.5" x2="16" y2="16" stroke="#555" stroke-width="2.4" stroke-linecap="round"/></svg>
  </div>
  <nav class="main-nav">
    <a href="#" style="width:126px">Home</a>
    <a href="#" style="width:127px">Services</a>
    <a href="#" style="width:137px">Prices</a>
    <a href="#" style="width:149px">Contact Us</a>
  </nav>
</header>

<section class="hero" role="img" aria-label="Photo of a bright, clean office with a water cooler, wooden desk and black leather chair">
  <div class="hero__dots"><span></span><span></span><span class="is-active"></span><span></span><span></span></div>
</section>

<section class="info-panel">
  <h2 class="section-title quote-title">Quick Quote</h2>
  <div class="field field--name">Name</div>
  <div class="field field--email">E mail</div>
  <div class="field field--message">Message</div>
  <div class="submit-button">Submit</div>

  <h2 class="section-title services-title">Services</h2>
  <div class="services-rule"></div>
  <div class="services-photo" role="img" aria-label="Photo of a tidy living room with a sofa and wooden floor"></div>
  <div class="services-copy">
    <div class="types"><span>Bi-weekly cleans,</span><span>One-off cleans,</span><span>Spring cleans,</span></div>
    <div class="types"><span>End of tenancy cleans,</span><span>After builders cleans</span></div>
    <p class="desc">In order for us to understand exactly what you would like us to do, one of our team can visit you in-home at a time which is convenient for you to discuss your requirements.</p>
    <a class="read-more" href="#">Read More</a>
  </div>
</section>

<section class="welcome">
  <h1 class="welcome__title">Welcome to our site</h1>
  <p class="welcome__text">Welcome to our website, we are a premier domestic cleaning company based in Hollowbrook, Wessex. Our vision is to supply households with a quality, tailored cleaning service, freeing up individuals spare time and replacing the stereotypical unreliable, inconsistent cleaners.</p>
  <p class="welcome__perks">No contracts<span class="sep">|</span> Insured<span class="sep">|</span> Free quotes<span class="sep">|</span> Personalised service<span class="sep">|</span> We supply all equipment at no extra cost<span class="sep">|</span> Hassel free service</p>
</section>

<footer class="site-footer">
  <div class="footer-links">
    <div>Home<span class="sep">|</span>Services<span class="sep">|</span>Prices<span class="sep">|</span>Contact Us</div>
    <div>Office cleaning<span class="sep">|</span>Apartment cleaning<span class="sep">|</span>Business place cleaning<span class="sep">|</span>Shopping mall cleaning</div>
    <div>Copyrights @ 2012 All Rights Reserved</div>
  </div>
  <div class="footer-contact">
    <div>Telephone: 07700 900462</div>
    <div>Email: hello@brookfieldcleaners.example</div>
  </div>
</footer>

<div class="edge-bar edge-bar--bottom"></div>
</body>
</html>
```